Business Card Design Project

- makeup artist business card

- original and creative

- Elegant design

- Feel free to come out with cool designs but stick to being elegant and attractive

- Design relates to makeup

- includes name, occupation, contact numbers, email, website

- regular size business card

- round corner card

- double sided

- on 1 side it should just have the website name in the center " browsandblush.example "

Industry/Entity Type

Business

Requirements
Must have
• Marla Voss
Makeup Artist
USA: +1 (415)872-6410
Singapore: +65 83027715
marlavoss@browsandblush.example
www.browsandblush.example
Should not have
• nothing cartoon looking.
Pictures of makeup being grab from the internet.. Examples: eyes or lips.

```html
<!DOCTYPE html>
<html lang="en">
<head>
<meta charset="utf-8">
<title>Marla Voss – Makeup Artist Business Card</title>
<link rel="stylesheet" href="https://fonts.googleapis.com/css2?family=Arimo:wght@400&family=Yellowtail&display=swap">
<style>
  :root {
    --page-bg: #ffffff;
    --card-white: #ffffff;
    --ink-crimson: #9b1b30;
    --photo-deep: #0f1d2b;
    --photo-teal: #2c4a5a;
    --photo-mid: #1d3443;
    --photo-red: #6e1420;
    --script-white: #ffffff;
    --card-shadow: rgba(0, 0, 0, 0.45);
  }
  html, body {
    margin: 0;
    padding: 0;
    width: 1200px;
    height: 900px;
    overflow: hidden;
    background: var(--page-bg);
  }
  .canvas {
    position: relative;
    width: 1200px;
    height: 900px;
  }
  .card {
    position: absolute;
    top: 304px;
    width: 508px;
    height: 292px;
    border-radius: 28px;
    box-shadow: 8px 10px 14px var(--card-shadow);
    overflow: hidden;
  }
  .card--front {
    left: 84px;
    background: var(--card-white);
    box-shadow: 8px 10px 14px var(--card-shadow), inset 0 0 0 1px #e4e4e4;
  }
  .card--back {
    left: 608px;
  }
  .contact {
    position: absolute;
    left: 232px;
    top: 158px;
    font-family: "Arimo", Arial, sans-serif;
    font-style: normal;
    color: var(--ink-crimson);
    white-space: nowrap;
    margin: 0;
  }
  .contact__name,
  .contact__role {
    font-size: 18px;
    line-height: 22px;
    margin: 0;
  }
  .contact__details {
    margin: 12px 0 0;
    padding: 0;
    list-style: none;
    font-size: 15px;
    line-height: 21px;
  }
  .back__photo {
    position: absolute;
    inset: 0;
    background:
      radial-gradient(ellipse 22% 45% at 52% 60%, var(--photo-red) 0%, rgba(110, 20, 32, 0) 100%),
      linear-gradient(90deg, var(--photo-deep) 0%, var(--photo-teal) 22%, var(--photo-mid) 45%, #162a37 62%, var(--photo-teal) 80%, var(--photo-deep) 100%);
  }
  .back__website {
    position: absolute;
    left: 0;
    right: 0;
    top: 136px;
    text-align: center;
    font-family: "Yellowtail", cursive;
    font-size: 31px;
    line-height: 36px;
    color: var(--script-white);
    white-space: nowrap;
    margin: 0;
  }
</style>
</head>
<body>
  <main class="canvas">
    <section class="card card--front" aria-label="Card front: contact details">
      <address class="contact">
        <p class="contact__name">Marla Voss</p>
        <p class="contact__role">Makeup Artist</p>
        <ul class="contact__details">
          <li>USA: +1 (415)872-6410</li>
          <li>Singapore: +65 83027715</li>
          <li>marlavoss@browsandblush.example</li>
        </ul>
      </address>
    </section>

    <section class="card card--back" aria-label="Card back: website">
      <div class="back__photo" role="img" aria-label="Moody fashion photograph of a model in a red jacket posing in a dim blue-teal doorway"></div>
      <p class="back__website">www.browsandblush.example</p>
    </section>
  </main>
</body>
</html>
```